Modern Design Business Card industrial maintenance company

Business card design for Company named Brookvale Equipment Services

Target Market(s)

Industrial

Industry/Entity Type

Maintenance and repair

Contact Information for Business Card

Place holder for address, office phone, mobile number and email

Requirements
Must have
• Clean modern look
Nice to have
• N/a

```html
<!DOCTYPE html>
<html lang="en">
<head>
<meta charset="utf-8">
<title>Brookvale Equipment Services – Business Card</title>
<link href="https://fonts.googleapis.com/css2?family=Montserrat:wght@400;600;700&display=swap" rel="stylesheet">
<style>
  :root {
    --backdrop: #d4d6d6;
    --card: #f7f7f5;
    --ink: #111111;
    --ink-soft: #3a3a3a;
    --band-text: #d9d9d9;
  }
  * { box-sizing: border-box; margin: 0; padding: 0; }
  html, body { width: 1200px; height: 829px; overflow: hidden; }
  body {
    background: var(--backdrop);
    font-family: "Montserrat", sans-serif;
    color: var(--ink);
    position: relative;
  }
  .card {
    position: absolute;
    top: 260px;
    width: 540px;
    height: 309px;
    background: var(--card);
    box-shadow: 0 6px 18px rgba(0,0,0,0.12);
  }
  .card--front { left: 40px; }
  .card--back { left: 620px; }

  .brand {
    position: absolute;
    display: flex;
    align-items: center;
    gap: 12px;
  }
  .brand__mark {
    border: 3px solid var(--ink);
    border-radius: 50%;
    flex: none;
  }
  .brand__name {
    font-weight: 700;
    text-transform: uppercase;
    line-height: 1.05;
    color: var(--ink);
  }
  .card--front .brand { left: 150px; top: 44px; }
  .card--front .brand__mark { width: 56px; height: 56px; }
  .card--front .brand__name { font-size: 19px; letter-spacing: 1.5px; }

  .card--back .brand { left: 92px; top: 112px; }
  .card--back .brand__mark { width: 76px; height: 76px; }
  .card--back .brand__name { font-size: 26px; letter-spacing: 2px; }

  .holder {
    position: absolute;
    right: 300px;
    top: 140px;
    text-align: right;
  }
  .holder__name { font-weight: 700; font-size: 17px; letter-spacing: 0.5px; }
  .holder__role { font-size: 11px; color: var(--ink-soft); margin-top: 2px; }

  .divider {
    position: absolute;
    left: 258px;
    top: 140px;
    width: 1px;
    height: 70px;
    background: var(--ink-soft);
  }

  .contacts {
    position: absolute;
    left: 272px;
    top: 144px;
    list-style: none;
    font-size: 12.5px;
    color: var(--ink-soft);
  }
  .contacts li { display: flex; align-items: center; gap: 7px; height: 21px; }
  .contacts svg { width: 11px; height: 11px; fill: var(--ink); flex: none; }

  .address-band {
    position: absolute;
    left: 0; right: 0;
    top: 236px;
    height: 30px;
    background: var(--ink);
    color: var(--band-text);
    font-size: 12px;
    display: flex;
    align-items: center;
    padding-left: 40px;
    letter-spacing: 0.3px;
  }
</style>
</head>
<body>
  <section class="card card--front" aria-label="Business card front">
    <div class="brand">
      <span class="brand__mark"></span>
      <span class="brand__name">Brookvale<br>Equipment Services</span>
    </div>

    <div class="holder">
      <p class="holder__name">DANIEL HARROW</p>
      <p class="holder__role">Owner &amp; Manager</p>
    </div>

    <span class="divider"></span>

    <ul class="contacts">
      <li>
        <svg viewBox="0 0 16 16"><path d="M3.5 1l3 3-1.8 1.8c.9 2 2.5 3.6 4.5 4.5L11 8.5l3 3-2 2.5C6.5 13.5 2.5 9.5 1 3.5z"/></svg>
        5310 - 672 - 4189
      </li>
      <li>
        <svg viewBox="0 0 16 16"><path d="M1 3h14v10H1z M2 4l6 5 6-5" fill="none" stroke="#111" stroke-width="1.6"/></svg>
        info@brookvaleequipment.com
      </li>
      <li>
        <svg viewBox="0 0 16 16"><circle cx="8" cy="8" r="6.5" fill="none" stroke="#111" stroke-width="1.6"/><path d="M1.5 8h13M8 1.5c-3 3.5-3 9.5 0 13M8 1.5c3 3.5 3 9.5 0 13" fill="none" stroke="#111" stroke-width="1.2"/></svg>
        www.brookvaleequipment.com
      </li>
    </ul>

    <div class="address-band">P.O. Box Linden Street Country Name AB, K7R 2M9</div>
  </section>

  <section class="card card--back" aria-label="Business card back">
    <div class="brand">
      <span class="brand__mark"></span>
      <span class="brand__name">Brookvale<br>Equipment Services</span>
    </div>
  </section>
</body>
</html>
```